Ferncrest Dental, LLC business card project

Business card to be designed with current logo.
Dental office- please keep design of card that looks clean and professional.
Please include the following info:
Ferncrest Dental, LLC
Dr. Lorna Pettigrew
2871 Marlowe Street
Bethlehem, PA 18093
610-555-0193
ferncrestdental.office@examplemail.test
Hello everyone-
Reason: Just got back from overseas- will look at all designs and provide feedback. Thank you!
Reason: Polling my friends for the final selection-
thank you to all those that participated- so many talented designers!

```html
<!DOCTYPE html>
<html lang="en">
<head>
<meta charset="utf-8">
<title>Ferncrest Dental, LLC – Business Card</title>
<link rel="stylesheet" href="https://fonts.googleapis.com/css2?family=Poppins:wght@300;400;600&display=swap">
<style>
  :root {
    --leaf: #a4c639;
    --leaf-deep: #8fb02c;
    --paper: #ffffff;
    --ink: #3a3a3a;
    --ink-soft: #555555;
    --rule: #7a7a7a;
    --backdrop: #e4e4e4;
    --tooth-tone: #ececec;
    --tooth-shade: #d9d9d9;
  }
  html, body {
    margin: 0;
    padding: 0;
    width: 1200px;
    height: 914px;
    overflow: hidden;
    background: var(--backdrop);
    font-family: "Poppins", sans-serif;
  }
  .canvas {
    position: relative;
    width: 1200px;
    height: 914px;
  }
  .card {
    position: absolute;
    left: 270px;
    width: 660px;
    height: 377px;
    box-shadow: 0 6px 18px rgba(0,0,0,0.18);
    overflow: hidden;
  }

  /* Back of card */
  .card-back {
    top: 48px;
    background: var(--leaf);
    display: flex;
    align-items: center;
    justify-content: center;
    gap: 18px;
  }
  .brand-mark {
    width: 40px;
    height: 40px;
    border-radius: 50%;
    background: var(--paper);
    flex: none;
  }
  .brand-name {
    color: var(--paper);
    font-weight: 300;
    font-size: 44px;
    letter-spacing: 0.5px;
    margin: 0;
  }

  /* Front of card */
  .card-front {
    top: 489px;
    background: var(--paper);
  }
  .edge-band {
    position: absolute;
    left: 0;
    top: 0;
    width: 12px;
    height: 100%;
    background: var(--leaf);
  }
  .edge-pointer {
    position: absolute;
    left: 12px;
    top: 131px;
    width: 0;
    height: 0;
    border-top: 12px solid transparent;
    border-bottom: 12px solid transparent;
    border-left: 12px solid var(--leaf);
  }
  .rule {
    position: absolute;
    height: 1px;
    background: var(--rule);
  }
  .rule-upper { left: 45px; top: 200px; width: 250px; }
  .rule-lower { left: 45px; top: 286px; width: 595px; }

  .artwork {
    position: absolute;
    left: 305px;
    top: 36px;
    width: 290px;
    height: 215px;
    border-radius: 18px;
    background: linear-gradient(90deg, var(--leaf) 0%, var(--leaf) 40%, var(--tooth-tone) 58%, var(--tooth-shade) 100%);
  }

  .holder-name {
    position: absolute;
    left: 45px;
    top: 126px;
    margin: 0;
    font-size: 23px;
    line-height: 32px;
    color: var(--ink);
    font-weight: 600;
    white-space: nowrap;
  }
  .holder-name .title {
    font-weight: 300;
    color: var(--ink-soft);
  }
  .contact {
    position: absolute;
    left: 45px;
    top: 212px;
    margin: 0;
    padding: 0;
    list-style: none;
    font-size: 11.5px;
    color: var(--ink);
    line-height: 22px;
  }
  .contact li {
    display: flex;
    align-items: center;
    gap: 8px;
    white-space: nowrap;
  }
  .contact svg { flex: none; }
  .address {
    position: absolute;
    right: 40px;
    top: 298px;
    margin: 0;
    font-style: normal;
    text-align: right;
    font-size: 13px;
    line-height: 20px;
    color: var(--ink);
  }
</style>
</head>
<body>
<main class="canvas">

  <section class="card card-back">
    <span class="brand-mark" aria-hidden="true"></span>
    <p class="brand-name">Ferncrest Dental, LLC</p>
  </section>

  <section class="card card-front">
    <div class="edge-band"></div>
    <div class="edge-pointer"></div>

    <div class="artwork" role="img" aria-label="Brand illustration area: two green trees on a rising green hill beside a large white tooth"></div>

    <div class="rule rule-upper"></div>
    <div class="rule rule-lower"></div>

    <h1 class="holder-name"><span class="title">Dr.</span> Lorna Pettigrew</h1>

    <ul class="contact">
      <li>
        <svg width="11" height="11" viewBox="0 0 24 24" aria-hidden="true"><path fill="var(--leaf-deep)" d="M6.6 10.8a15.1 15.1 0 0 0 6.6 6.6l2.2-2.2a1 1 0 0 1 1-.25 11.4 11.4 0 0 0 3.6.57 1 1 0 0 1 1 1V20a1 1 0 0 1-1 1A17 17 0 0 1 3 4a1 1 0 0 1 1-1h3.5a1 1 0 0 1 1 1c0 1.25.2 2.45.57 3.6a1 1 0 0 1-.25 1z"/></svg>
        610-555-0193
      </li>
      <li>
        <svg width="11" height="9" viewBox="0 0 24 18" aria-hidden="true"><rect width="24" height="18" rx="2" fill="var(--leaf-deep)"/><path d="M2 2l10 8 10-8" fill="none" stroke="#fff" stroke-width="2"/></svg>
        ferncrestdental.office@examplemail.test
      </li>
    </ul>

    <address class="address">
      2871 Marlowe Street<br>
      Bethlehem, PA 18093
    </address>
  </section>

</main>
</body>
</html>
```